Law Firm Needs a new Website Design

We need a new website design for our law firm located in Manhattan (Law Offices of Tobias R. Venkland, PLLC).
We have an existing logo that we will to continue using, which can be found in www.VenklandLaw.example.
The Prime Counsel, Top Advocates Logo should also be reflected near the bottom of the Home page.
The website will be 6 pages.

Deliverables:
I want a
1) home page,
2) About Us/Practice Areas page,
3) attorneys,
4) News and Articles page, and
5) Contact and Directions/Privacy Policy page.

The colors of my logo should be in the website.
I also like a touch of black and red.

The website should project "excellence."
We seek to provide the highest quality legal services.
We handle estate planning, wills, trusts, planning for people with disabilities, asset protection and preservation, Medicaid planning, hospital safe discharge, nursing home placement, powers of attorney, health care proxies, living wills, guardianships, probate, estate administration and related litigation.

I would like the colors of my Logo used (including shading where appropriate).
I also want some black on the borders and/or bottom and some red touches throughout the page.

My Logo should appear everywhere that "Law Offices Of Tobias R. Venkland, PLLC" appears.
I want the badges for Prime counsel, Top Advocates, Top Legal Practices, and ZELQ on the Home page.
I do not want too much text on the home page.

We would also like the website to have coding.
The final design should also communicate quality, expertise and stability.
Great start so far by the people who submitted designs.
Thank you.

Industry/Entity Type

Law Firm

Coding

Coded - Design and coding required

Number of Pages Required

5+ page

Colors
3276b5
ec1f27
474747

Requirements
Must have
• Please use my logo each time you mention Law Offices of Tobias R. Venkland, PLLC. Please include the Primecounsel, Top Advocates, Top Legal Practices and Zelq rating Badges on the web home page. I only wish to be contacted by phone. I am not including testimonials and am only using the New York City address.
Nice to have
• Prefer illustrations to photos regarding practice areas
Should not have
• Testimonials, contact me by email, free consultation.

```html
<!DOCTYPE html>
<html lang="en">
<head>
<meta charset="utf-8">
<title>Law Offices of Tobias R. Venkland, PLLC</title>
<link rel="stylesheet" href="https://fonts.googleapis.com/css2?family=Roboto:wght@300;400;500;700&family=Covered+By+Your+Grace&display=swap">
<style>
:root{
  --blue:#3276b5;
  --blue-dark:#1d2f57;
  --navy:#253a66;
  --red:#ec1f27;
  --ink:#474747;
  --muted:#6b6b6b;
  --paper:#f4f5f7;
  --white:#ffffff;
  --footer:#33373d;
  --footer-text:#b9bcc1;
}
*{box-sizing:border-box;margin:0;padding:0}
html,body{width:1200px;height:2261px;overflow:hidden}
body{font-family:"Roboto",Arial,sans-serif;color:var(--ink);background:var(--white);position:relative}

.site-header{height:88px;background:var(--white);display:flex;align-items:center;justify-content:center;gap:12px}
.brand-mark{width:30px;height:30px;background:var(--navy)}
.brand-name{font-family:"Roboto",Arial,sans-serif;font-weight:500;font-size:22px;color:var(--navy);letter-spacing:.3px}

.hero{position:relative;height:568px;background:linear-gradient(160deg,#3b4d80 0%,#25345e 45%,#1a2647 100%);color:var(--white);text-align:center}
.main-nav{height:70px;background:rgba(255,255,255,.08);display:flex;justify-content:center;align-items:center;gap:38px;font-size:15px;letter-spacing:.3px}
.main-nav a{color:var(--white);text-decoration:none}
.main-nav a.is-active{color:var(--red)}
.award-badge{position:absolute;left:15px;top:75px;width:103px;height:131px;background:var(--white);border-radius:4px}
.award-badge::after{content:"";position:absolute;left:-4px;right:-4px;top:88px;height:22px;background:var(--blue)}
.hero-title{font-family:"Covered By Your Grace",cursive;font-weight:400;font-size:70px;line-height:1.02;padding-top:142px;letter-spacing:2px}
.hero-sub{font-size:20px;margin-top:28px}
.hero-actions{margin-top:30px;display:flex;justify-content:center;gap:16px}
.btn{font-size:9.5px;font-weight:700;text-transform:uppercase;padding:0 14px;height:34px;display:inline-flex;align-items:center;border-radius:3px;color:var(--white)}
.btn-solid{background:var(--blue)}
.btn-ghost{border:1.5px solid var(--white)}

.practice-band{height:208px;background:var(--blue);display:flex;justify-content:center;align-items:center}
.practice-item{width:176px;height:142px;display:flex;flex-direction:column;align-items:center;justify-content:center;gap:16px;color:var(--white);font-weight:700;font-size:15px;text-transform:uppercase;border-right:1px solid rgba(255,255,255,.25)}
.practice-item:last-child{border-right:0}
.practice-item svg{width:62px;height:62px;fill:none;stroke:var(--white);stroke-width:2}

.section-title{text-align:center;color:var(--blue);font-size:22px;font-weight:700;padding-bottom:14px;margin:0 54px;border-bottom:1.5px dashed var(--blue)}
.firm-profile{height:373px;background:var(--paper);padding-top:20px}
.profile-copy{width:1094px;margin:46px auto 0;text-align:center;font-size:12.4px;line-height:1.55;color:var(--muted)}
.profile-copy p+p{margin-top:17px}
.profile-copy .founder{color:var(--red)}
.rating-badges{display:flex;justify-content:center;gap:10px;margin-top:22px}
.rating-badges span{height:30px;display:block}
.rating-badges .badge-a{width:140px;background:#e6e9ef;border-left:22px solid var(--navy)}
.rating-badges .badge-b{width:230px;background:var(--blue);border-radius:3px}
.rating-badges .badge-c{width:140px;background:#d9c27a}

.columns-band{height:274px;background:linear-gradient(170deg,#2e3f6e 0%,#233360 50%,#1b2749 100%)}

.attorneys{height:446px;background:var(--white);padding-top:14px}
.attorney-grid{position:relative}
.attorney{position:absolute;top:46px;display:flex;gap:52px}
.attorney-photo{width:190px;height:273px;border:4px solid #c9c9c9;background:linear-gradient(180deg,#7b8494 0%,#b6a690 100%);box-shadow:0 0 0 1px #999}
.attorney-one{left:93px}
.attorney-two{left:642px}
.attorney-body{width:270px;padding-top:0}
.attorney-name{color:var(--blue);font-size:19px;font-weight:400;margin-top:-8px}
.attorney-role{font-size:12.5px;color:var(--muted);margin-top:12px;padding-bottom:10px;border-bottom:1px dotted #bbb;width:140px}
.attorney-bio{font-size:12.4px;line-height:1.55;color:var(--muted);margin-top:16px;height:210px}
.btn-bio{background:var(--blue);color:var(--white);font-size:12px;font-weight:700;height:33px;padding:0 20px;display:inline-flex;align-items:center;border-radius:3px;margin-top:12px}

.site-footer{height:304px;background:var(--footer);color:var(--footer-text);position:relative}
.footer-cols{position:absolute;top:52px;left:0;width:100%}
.footer-col{position:absolute;width:250px;font-size:12.5px;line-height:1.55}
.footer-col h3{color:var(--white);font-size:18px;font-weight:700;margin-bottom:22px}
.footer-col p+p{margin-top:18px}
.footer-col strong{color:var(--white);font-weight:400}
.col-contact{left:53px}.col-phone{left:333px}.col-manhattan{left:615px}.col-island{left:896px}
.footer-rule{position:absolute;left:53px;right:53px;top:245px;border-top:1px solid #4a4f56}
.copyright{position:absolute;bottom:12px;width:100%;text-align:center;font-size:12.5px}
</style>
</head>
<body>

<header class="site-header">
  <span class="brand-mark"></span>
  <span class="brand-name">Law Offices of Tobias R. Venkland, PLLC</span>
</header>

<section class="hero" role="img" aria-label="Courthouse columns against a cloudy sky in deep blue tones">
  <nav class="main-nav">
    <a class="is-active">HOME</a><a>ABOUT US</a><a>ATTORNEYS</a><a>NEWS</a><a>ARTICLES</a><a>CONTACT AND DIRECTIONS</a>
  </nav>
  <div class="award-badge" role="img" aria-label="Law firm ranking badge"></div>
  <h1 class="hero-title">Welcome to<br>Tobias R. Venkland</h1>
  <p class="hero-sub">Law Office of PLLC</p>
  <div class="hero-actions">
    <span class="btn btn-solid">I like it! Purchase</span>
    <span class="btn btn-ghost">Go on surfing</span>
  </div>
</section>

<section class="practice-band">
  <div class="practice-item">
    <svg viewBox="0 0 64 64"><circle cx="30" cy="34" r="22"/><circle cx="30" cy="34" r="14"/><circle cx="30" cy="34" r="6"/><path d="M30 34 L54 10 M48 10 h6 v6"/></svg>Bankrupcy</div>
  <div class="practice-item">
    <svg viewBox="0 0 64 64"><path d="M14 30 L19 17 h26 l5 13"/><rect x="8" y="30" width="48" height="16" rx="3"/><rect x="12" y="46" width="8" height="6"/><rect x="44" y="46" width="8" height="6"/><circle cx="16" cy="38" r="3"/><circle cx="48" cy="38" r="3"/><path d="M24 38 h16"/></svg>Traffic Tikets</div>
  <div class="practice-item">
    <svg viewBox="0 0 64 64"><path d="M32 6 v50 M14 14 h36 M22 56 h20"/><path d="M14 14 L6 36 h16 Z M50 14 L42 36 h16 Z"/></svg>Personal Injury</div>
  <div class="practice-item">
    <svg viewBox="0 0 64 64"><path d="M6 22 L32 8 L58 22 Z M8 24 h48 M8 54 h48 M6 58 h52"/><path d="M16 28 v22 M26 28 v22 M38 28 v22 M48 28 v22"/></svg>Estate Planning</div>
  <div class="practice-item">
    <svg viewBox="0 0 64 64"><path d="M14 30 L19 17 h26 l5 13"/><rect x="8" y="30" width="48" height="16" rx="3"/><rect x="12" y="46" width="8" height="6"/><rect x="44" y="46" width="8" height="6"/><circle cx="16" cy="38" r="3"/><circle cx="48" cy="38" r="3"/><path d="M24 38 h16"/></svg>Car Accidents</div>
  <div class="practice-item">
    <svg viewBox="0 0 64 64"><circle cx="30" cy="34" r="22"/><circle cx="30" cy="34" r="14"/><circle cx="30" cy="34" r="6"/><path d="M30 34 L54 10 M48 10 h6 v6"/></svg>Capital Market</div>
</section>

<section class="firm-profile">
  <h2 class="section-title">Firm Profile</h2>
  <div class="profile-copy">
    <p>Our firm was founded in 1993 by <span class="founder">Tobias R. Venkland</span>, a member of the National Guild of Elder Care Counsel (NGECC) and an elder law practitioner for over 19 years. Our firm is uniquely positioned to provide quality legal advice and representation in regards to estate planning, wills, trusts, planning for people with disabilities, asset protection and preservation, Medicaid planning, hospital safe discharge, nursing home placement, powers of attorney, health care proxies, living wills, guardianships, probate, estate administration and related litigation.</p>
    <p>Our familiarity with entitlement programs such as Medicaid and the statutes and regulations pertaining to them, our sensitivity to the problems and needs of seniors and our access to geriatric care managers enable us to help families preserve their life savings while planning for the care of a spouse, a parent or loved one who has dementia, Alzheimer's or other long-term health care needs.</p>
    <p>We care about our clients and believe in cultivating long-term relationships. We strive to maintain the dignity, independence and well-being of our clients and respond to them quickly with the consideration and respect they deserve.</p>
  </div>
  <div class="rating-badges">
    <span class="badge-a" role="img" aria-label="Top Advocates rating badge"></span>
    <span class="badge-b" role="img" aria-label="Firm rating badge"></span>
    <span class="badge-c" role="img" aria-label="Prime Counsel rating badge"></span>
  </div>
</section>

<section class="columns-band" role="img" aria-label="Classical stone columns in deep blue tones"></section>

<section class="attorneys">
  <h2 class="section-title">Attorneys</h2>
  <div class="attorney-grid">
    <article class="attorney attorney-one">
      <div class="attorney-photo" role="img" aria-label="Portrait of Tobias R. Venkland"></div>
      <div class="attorney-body">
        <h3 class="attorney-name">Tobias R. Venkland</h3>
        <p class="attorney-role">Founder</p>
        <p class="attorney-bio">Was chair of the Metro County Bar Association pro bono Elder Law Project and the past chair of the Metro County Bar Association Elder Law Committee. Mr. Venkland is an adjunct assistant professor at Eastbridge University School of Continuing and Professional Studies where he teaches a course in Trusts and Estates and the Eastbridge Harwell School of Lifelong Learning where he teaches an Elder Law class.</p>
        <span class="btn-bio">READ BIO</span>
      </div>
    </article>
    <article class="attorney attorney-two">
      <div class="attorney-photo" role="img" aria-label="Portrait of Marisol Kent Venkland"></div>
      <div class="attorney-body">
        <h3 class="attorney-name">Marisol Kent Venkland</h3>
        <p class="attorney-role">Co-Founder</p>
        <p class="attorney-bio">Is a graduate of Northfield University and the Halvorsen School of Law where she participated in the Family Law Clinic. Before joining the firm in 2008, Ms. Venkland was a trial attorney for the Kingsbay Family Court Legal Services office prosecuting civil child abuse and neglect cases for the Commissioner of the Office for Family Services for five years</p>
        <span class="btn-bio">READ BIO</span>
      </div>
    </article>
  </div>
</section>

<footer class="site-footer">
  <div class="footer-cols">
    <div class="footer-col col-contact">
      <h3>Contact</h3>
      <p>Please feel free to contact us for any issue. Our staff is available to you from 9AM until 5PM on weekdays.</p>
    </div>
    <div class="footer-col col-phone">
      <h3>Phone number</h3>
      <p><strong>Manhattan:</strong> (212) 555-0148</p>
      <p><strong>Long Island:</strong> (212) 555-0148</p>
    </div>
    <div class="footer-col col-manhattan">
      <h3>Office Manhattan</h3>
      <p><strong>Address:</strong> 218 Harlow Avenue Suite 1400</p>
      <p><strong>City:</strong> New York, NY 10099</p>
    </div>
    <div class="footer-col col-island">
      <h3>Office Long Island</h3>
      <p><strong>Address:</strong> 77 Bramble Avenue</p>
      <p><strong>City:</strong> Suite 300</p>
    </div>
  </div>
  <div class="footer-rule"></div>
  <p class="copyright">Copyrights© 2009-2016 Law Offices of Tobias R. Venkland, PLLC</p>
</footer>

</body>
</html>
```